upolstery Business Card Design

Antique furniture restoration, motor and marine trimming, canvas work ,cafe blinds,

Industry/Entity Type

Business

Contact Information for Business Card

RK UPOLSTERY & CANVAS
42 TOLAN ST WILLIAMS
Callum Brennick PH:0431562907
brk58@vextonmail.com

```html
<!DOCTYPE html>
<html lang="en">
<head>
<meta charset="utf-8">
<title>RK Trim &amp; Canvas Works – Business Card</title>
<link href="https://fonts.googleapis.com/css2?family=Jost:wght@400;500&display=swap" rel="stylesheet">
<style>
  :root {
    --card-blue: #2f55b8;
    --card-blue-deep: #2242a0;
    --card-blue-light: #4a73d2;
    --panel-white: rgba(238, 241, 250, 0.78);
    --ink-indigo: #3b3f9e;
    --title-white: #ffffff;
  }
  * { margin: 0; padding: 0; box-sizing: border-box; }
  html, body {
    width: 1200px;
    height: 761px;
    overflow: hidden;
    background: #ffffff;
  }
  .card {
    position: relative;
    width: 1200px;
    height: 761px;
    overflow: hidden;
    font-family: "Jost", "Futura", sans-serif;
    background: var(--card-blue);
  }
  .card__artwork {
    position: absolute;
    inset: 0;
    background:
      radial-gradient(ellipse at 55% 40%, var(--card-blue-light) 0%, rgba(74,115,210,0) 60%),
      linear-gradient(160deg, var(--card-blue-deep) 0%, var(--card-blue) 50%, var(--card-blue-deep) 100%);
  }
  .card__title {
    position: absolute;
    left: 112px;
    top: 14px;
    font-size: 74px;
    font-weight: 400;
    letter-spacing: 1px;
    line-height: 1.2;
    color: var(--title-white);
    white-space: nowrap;
  }
  .info-panel {
    position: absolute;
    left: 4px;
    top: 281px;
    width: 1194px;
    height: 362px;
    border-radius: 32px;
    background: var(--panel-white);
  }
  .contact-list {
    position: absolute;
    left: 62px;
    top: 65px;
    list-style: none;
    color: var(--ink-indigo);
  }
  .contact-list__item {
    display: flex;
    align-items: center;
    height: 72px;
    font-size: 48px;
    font-weight: 400;
    white-space: nowrap;
  }
  .contact-list__icon {
    width: 44px;
    height: 44px;
    margin-right: 10px;
    flex: none;
  }
  .services {
    position: absolute;
    left: 600px;
    top: 57px;
    width: 604px;
    text-align: center;
    color: var(--ink-indigo);
    font-size: 37px;
    font-weight: 400;
    line-height: 43px;
    white-space: nowrap;
  }
</style>
</head>
<body>
  <div class="card">
    <div class="card__artwork" role="img" aria-label="Blueprint-style floor plan of sofas and armchairs in blue tones"></div>

    <h1 class="card__title">RK TRIM &amp; CANVAS WORKS</h1>

    <section class="info-panel">
      <ul class="contact-list">
        <li class="contact-list__item">
          <svg class="contact-list__icon" viewBox="0 0 40 40" aria-hidden="true">
            <path d="M20 4c-6 0-10.5 4.5-10.5 10.3C9.5 21.5 20 31 20 31s10.5-9.5 10.5-16.7C30.5 8.5 26 4 20 4z" fill="var(--ink-indigo)"/>
            <circle cx="20" cy="14.5" r="4" fill="#eef1fa"/>
            <ellipse cx="20" cy="33" rx="13" ry="4" fill="none" stroke="var(--ink-indigo)" stroke-width="2.5"/>
          </svg>
          <span>42 Tolan St Kerrigan</span>
        </li>
        <li class="contact-list__item">
          <svg class="contact-list__icon" viewBox="0 0 40 40" aria-hidden="true">
            <circle cx="20" cy="20" r="17" fill="none" stroke="var(--ink-indigo)" stroke-width="2.5"/>
            <path d="M14 11.5c1-.8 2-.6 2.6.3l2 3c.5.8.3 1.7-.4 2.3l-1.3 1c.8 2 2.6 3.9 4.7 4.8l1-1.3c.6-.7 1.5-.9 2.3-.4l3 2c.9.6 1.1 1.7.3 2.6l-1.4 1.5c-1.2 1.2-3 1.4-4.6.7-4.7-2.1-8.2-5.6-10.3-10.3-.7-1.6-.5-3.4.7-4.6z" fill="var(--ink-indigo)"/>
          </svg>
          <span>0431562907</span>
        </li>
        <li class="contact-list__item">
          <svg class="contact-list__icon" viewBox="0 0 40 40" aria-hidden="true">
            <circle cx="20" cy="20" r="17" fill="none" stroke="var(--ink-indigo)" stroke-width="2.5"/>
            <rect x="10.5" y="13" width="19" height="14" rx="1.5" fill="var(--ink-indigo)"/>
            <path d="M11.5 14.5l8.5 6.5 8.5-6.5M11.5 26l6-5.5M28.5 26l-6-5.5" fill="none" stroke="#eef1fa" stroke-width="1.6"/>
          </svg>
          <span>brk58@vextonmail.com</span>
        </li>
      </ul>

      <div class="services">
        <p>Services:</p>
        <p>Antique Furniture Restoration,</p>
        <p>Motor And Marine Trimming</p>
        <p>Canvas Work ,</p>
        <p>Cafe Blinds,</p>
      </div>
    </section>
  </div>
</body>
</html>
```